create a Wedding Invitation design

Personalized wedding invitation using names, initials, a nice monogram with decorative border

incorporate names: Lena and Osmond (first names)
Halvorsk (surname)
and wedding date , April 12, 2014

Colors: black ink on white;
optional accent colors: bright pink, bright orange, cajun red (may be flowers)
No shades of Purple

Industry/Entity Type

Wedding

Requirements
Must have
• Romantic, slightly formal looking design, black on white ; some accent color preferred, monogram (using first names Lena and Osmond and last name Halvorsk), that could be isolated and used on RSVP cards preferred
Nice to have
• idea of being at the top of a building (venue is called Brightmoor Hall) - the wedding is being held on the 17th floor of building with panoramic views of Washington DC and the mountains ; Washington DC skyline, iconic DC cherry blossoms

Here are some examples of a typical Washington, DC skyline (this is an optional or secondary feature only - not to dominate the design):
http://www.pictovane.com/clip-art/washington-dc.html#comp.asp?recid=48113760&xtra=
Cherry blossoms : http://www.jaunterly.com/news/story_8146.html

```html
<!DOCTYPE html>
<html lang="en">
<head>
<meta charset="utf-8">
<title>Lena and Osmond — Wedding Invitation</title>
<link rel="stylesheet" href="https://fonts.googleapis.com/css2?family=Felipa&display=swap">
<style>
  :root {
    --ink: #0c0c0c;
    --paper: #ffffff;
    --echo: rgba(0, 0, 0, 0.22);
    --sky: #a9d3ee;
    --blossom: #e9a7b8;
    --blossom-deep: #d9849c;
    --branch: #5b4a48;
    --lawn: #5f9a3c;
    --lawn-deep: #3f7a25;
    --haze: #e9ecea;
  }
  html, body {
    margin: 0;
    padding: 0;
    width: 1200px;
    height: 800px;
    overflow: hidden;
    background: var(--paper);
  }
  .invitation {
    position: relative;
    width: 1200px;
    height: 800px;
    overflow: hidden;
    background: var(--paper);
    font-family: "Felipa", "Lucida Calligraphy", cursive;
    color: var(--ink);
  }
  .blossom-canopy {
    position: absolute;
    left: 0; top: 0;
    width: 1200px; height: 150px;
    background:
      radial-gradient(ellipse 140px 40px at 80px 80px, var(--blossom) 0%, transparent 70%),
      radial-gradient(ellipse 200px 45px at 1050px 50px, var(--blossom-deep) 0%, transparent 70%),
      radial-gradient(ellipse 180px 35px at 820px 95px, var(--blossom) 0%, transparent 70%),
      radial-gradient(ellipse 160px 30px at 330px 105px, var(--blossom) 0%, transparent 70%),
      radial-gradient(ellipse 120px 30px at 600px 110px, rgba(233,167,184,.6) 0%, transparent 70%),
      linear-gradient(to bottom, var(--sky) 0%, #cfe6f4 55%, var(--paper) 100%);
  }
  .lawn-horizon {
    position: absolute;
    left: 0; bottom: 0;
    width: 1200px; height: 100px;
    background:
      linear-gradient(172deg, transparent 60%, rgba(190,170,150,.55) 62%, transparent 66%),
      linear-gradient(to bottom, var(--paper) 0%, var(--haze) 14%, var(--lawn) 30%, var(--lawn-deep) 100%);
  }
  .headline {
    position: absolute;
    left: 0; top: 145px;
    width: 1200px;
    margin: 0;
    text-align: center;
    font-weight: 400;
    font-size: 80px;
    line-height: 1;
    text-shadow: 0 26px 5px var(--echo);
  }
  .lead-in {
    position: absolute;
    left: 333px; top: 250px;
    margin: 0;
    font-size: 48px;
    line-height: 1;
    text-shadow: 0 26px 5px var(--echo);
  }
  .monogram-frame {
    position: absolute;
    left: 380px; top: 338px;
    width: 454px; height: 316px;
  }
  .monogram-frame svg {
    position: absolute;
    inset: 0;
    width: 100%; height: 100%;
    overflow: visible;
  }
  .frame-echo {
    transform: translateY(34px);
    filter: blur(4px);
    opacity: .3;
  }
  .couple-names,
  .wedding-date {
    position: absolute;
    margin: 0;
    width: 100%;
    text-align: center;
    line-height: 1;
    text-shadow: 0 30px 4px var(--echo);
  }
  .couple-names {
    top: 92px;
    left: -14px;
    font-size: 53px;
  }
  .wedding-date {
    top: 166px;
    left: -4px;
    font-size: 35px;
  }
</style>
</head>
<body>
<main class="invitation">
  <div class="blossom-canopy" role="img" aria-label="Photograph of pink cherry blossom branches against a pale blue sky, fading into white"></div>

  <h1 class="headline">You are cordially invited</h1>
  <p class="lead-in">to the weddiing of</p>

  <section class="monogram-frame">
    <svg class="frame-echo" viewBox="0 0 460 320" aria-hidden="true">
      <defs>
        <path id="label-shape" d="M60,30 Q230,2 400,30 A30,30 0 0 0 430,60 Q458,160 430,260 A30,30 0 0 0 400,290 Q230,318 60,290 A30,30 0 0 0 30,260 Q2,160 30,60 A30,30 0 0 0 60,30 Z"/>
      </defs>
      <use href="#label-shape" fill="none" stroke="#000" stroke-width="8"/>
    </svg>
    <svg viewBox="0 0 460 320" aria-hidden="true">
      <g fill="none" stroke="var(--ink)">
        <use href="#label-shape" stroke-width="6" transform="translate(230 160) scale(1.03) translate(-230 -160)"/>
        <use href="#label-shape" stroke-width="2" transform="translate(230 160) scale(0.975 0.965) translate(-230 -160)"/>
        <use href="#label-shape" stroke-width="1.5" transform="translate(230 160) scale(0.945 0.925) translate(-230 -160)"/>
      </g>
    </svg>
    <p class="couple-names">Lena and Osmond</p>
    <p class="wedding-date">April 12th 2014</p>
  </section>

  <div class="lawn-horizon" role="img" aria-label="Photograph of a wide green lawn with a paved path under a hazy horizon"></div>
</main>
</body>
</html>
```